business card and flyer/pricelist

Business Name: Fern Locks Westbrook
new boutique salon run from home, using Australian owned natural products and colours, we need a flyer design to do a letter box drop to advertise the business as well as incorporating a price list on the front (single sided with writing on front and only colour on back)

The salon has a natural feel with light coloured timber chairs, bamboo timber bench top and shelving.

we are after a natural toned colour for the flyer, with possibly a brown/darkish colour writing

we are after a flyer that will also be able to use the design heading (business name) for business cards as well

feel free to look on my pintrest account to get a feel for my style under Marla Quenby.

I love simple clean and Natural looks.

Font styles to use
Script
Other font styles liked:
• SCRIPT HANDWRITTEN FONTS

Colors
cadf82
e9f1ce
5c5c5c
d3d3d3
add136
fee18a

Requirements
Must have
• NATURAL COLOURINGS, eg soft greens, browns,
white or off white background.
Should not have
• photos,

```html
<!DOCTYPE html>
<html lang="en">
<head>
<meta charset="utf-8">
<title>Fern Locks Westbrook – Price List</title>
<link href="https://fonts.googleapis.com/css2?family=Yesteryear&family=Marck+Script&display=swap" rel="stylesheet">
<style>
  :root {
    --backdrop: #2f2f2f;
    --bark: #6a5148;
    --bark-deep: #5b443c;
    --leaf: #add136;
    --leaf-soft: #cadf82;
    --mist: #e9f1ce;
    --butter: #fee18a;
    --ink: #1e1e1e;
    --white: #ffffff;
  }
  * { box-sizing: border-box; margin: 0; padding: 0; }
  html, body {
    width: 668px; height: 1200px; overflow: hidden;
    background: var(--backdrop);
  }
  .flyer {
    position: absolute; left: 88px; top: 62px;
    width: 502px; height: 1078px;
    background: var(--bark);
    overflow: hidden;
  }
  .flourish-top {
    position: absolute; left: 0; top: 0; width: 502px; height: 300px;
    background:
      radial-gradient(ellipse 60% 45% at 60% 20%, rgba(173,209,54,0.75), rgba(173,209,54,0) 70%),
      radial-gradient(ellipse 40% 40% at 95% 45%, rgba(173,209,54,0.55), rgba(173,209,54,0) 70%),
      radial-gradient(ellipse 40% 35% at 10% 70%, rgba(202,223,130,0.25), rgba(202,223,130,0) 70%);
  }
  .flourish-faint {
    position: absolute; left: 0; top: 480px; width: 502px; height: 520px;
    background:
      radial-gradient(ellipse 55% 45% at 55% 40%, rgba(150,120,100,0.35), rgba(150,120,100,0) 70%),
      radial-gradient(ellipse 35% 40% at 95% 80%, rgba(150,120,100,0.3), rgba(150,120,100,0) 70%);
  }
  .band { position: absolute; left: 0; width: 502px; }
  .band--butter { top: 168px; height: 45px; background: var(--butter); }
  .band--leaf { top: 926px; height: 67px; background: var(--leaf); }

  .label { position: absolute; }
  .label svg { position: absolute; inset: 0; }
  .label__content {
    position: absolute; inset: 0;
    display: flex; flex-direction: column; align-items: center; justify-content: center;
    text-align: center; color: var(--ink);
  }
  .label--brand { left: 17px; top: 103px; width: 333px; height: 180px; }
  .brand-name {
    font-family: "Yesteryear", cursive;
    font-size: 38px; line-height: 48px;
  }
  .label--contact { left: 117px; top: 876px; width: 258px; height: 160px; }
  .contact-name {
    font-family: "Yesteryear", cursive;
    font-size: 34px; line-height: 36px; margin-bottom: 2px;
  }
  .contact-line {
    font-family: "Marck Script", cursive;
    font-size: 19px; line-height: 27px; color: #2b2b2b;
  }

  .price-title {
    position: absolute; left: 0; top: 318px; width: 502px;
    text-align: center;
    font-family: "Marck Script", cursive;
    font-size: 60px; color: var(--butter);
  }
  .price-list {
    position: absolute; left: 30px; top: 422px; width: 434px;
    list-style: none;
    font-family: "Marck Script", cursive;
    font-size: 27px; color: var(--white);
  }
  .price-list li {
    display: flex; align-items: baseline; height: 48.3px;
  }
  .price-list .leader {
    flex: 1; margin: 0 2px;
    border-bottom: 2px dotted var(--white);
    transform: translateY(-4px);
  }
</style>
</head>
<body>
  <main class="flyer">
    <div class="flourish-top" role="img" aria-label="Green swirling floral flourish"></div>
    <div class="flourish-faint" role="img" aria-label="Faint tonal floral flourish"></div>

    <div class="band band--butter"></div>
    <div class="label label--brand">
      <svg viewBox="0 0 333 180" width="333" height="180">
        <path d="M26 4 H307 A22 22 0 0 0 329 26 V154 A22 22 0 0 0 307 176 H26 A22 22 0 0 0 4 154 V26 A22 22 0 0 0 26 4 Z" fill="var(--butter)" stroke="#2a2a2a" stroke-width="2"/>
        <path d="M32 14 H301 A20 20 0 0 0 319 32 V148 A20 20 0 0 0 301 166 H32 A20 20 0 0 0 14 148 V32 A20 20 0 0 0 32 14 Z" fill="var(--mist)" stroke="#2a2a2a" stroke-width="2"/>
      </svg>
      <div class="label__content">
        <p class="brand-name">Fern Locks<br>Westbrook</p>
      </div>
    </div>

    <h1 class="price-title">Price List</h1>
    <ul class="price-list">
      <li><span>Lorem ipsum</span><span class="leader"></span><span>$00.00</span></li>
      <li><span>Lorem ipsum</span><span class="leader"></span><span>$00.00</span></li>
      <li><span>Lorem ipsum</span><span class="leader"></span><span>$00.00</span></li>
      <li><span>Lorem ipsum</span><span class="leader"></span><span>$00.00</span></li>
      <li><span>Lorem ipsum</span><span class="leader"></span><span>$00.00</span></li>
      <li><span>Lorem ipsum</span><span class="leader"></span><span>$00.00</span></li>
      <li><span>Lorem ipsum</span><span class="leader"></span><span>$00.00</span></li>
      <li><span>Lorem ipsum</span><span class="leader"></span><span>$00.00</span></li>
      <li><span>Lorem ipsum</span><span class="leader"></span><span>$00.00</span></li>
    </ul>

    <div class="band band--leaf"></div>
    <div class="label label--contact">
      <svg viewBox="0 0 258 160" width="258" height="160">
        <path d="M22 4 H236 A18 18 0 0 0 254 22 V138 A18 18 0 0 0 236 156 H22 A18 18 0 0 0 4 138 V22 A18 18 0 0 0 22 4 Z" fill="var(--butter)" stroke="#2a2a2a" stroke-width="2"/>
        <path d="M28 13 H230 A16 16 0 0 0 245 28 V132 A16 16 0 0 0 230 147 H28 A16 16 0 0 0 13 132 V28 A16 16 0 0 0 28 13 Z" fill="var(--leaf)" stroke="#2a2a2a" stroke-width="1.5"/>
      </svg>
      <div class="label__content">
        <p class="contact-name">Marla Quenby</p>
        <p class="contact-line">address</p>
        <p class="contact-line">phone number</p>
        <p class="contact-line">email</p>
      </div>
    </div>
  </main>
</body>
</html>
```